Spice Mix Label Bottle Branding - Health and Weight Loss Mixes

The company is called ZestRow Spice Mix's. We've created 5 spice mixes using ingredients that promote health and weight loss. We already have a logo but now we need labels for our bottles. We would like to see designs that have the feel of health supplements (see attached examples)

We would like a different colour featured with each of our flavours.

Our flavours are:
-Golden Chai (Yellow)
-Mild Curry (Orange)
-Coffee Rub (brown)
-Garlic Oregano (Green)
-Taco (Blue)

Thank you!

Target Market(s)

Ages 22-35. Men and Female. Trendy, Hipster.

Industry/Entity Type

Food Production

Font styles to use
Sans Serif

Colors
f37122
0655a3
0692cd
9bcb3c
fbee3f

Requirements
Must have
• A different featured colour for each flavour.
• The ZestRow Spices Logo (attached)
• The slogan: "Weight Loss Ingredients"
• -Golden Chai (Yellow)
• -Mild Curry (Orange)
• -Coffee Rub (brown)
• -Garlic Oregano (Green)
• -Taco (Blue)
• Text Files attached.
Nice to have
• A black label with a featured colour for each of the spice mice flavours.
• 'No Salt added'

```html
<!DOCTYPE html>
<html lang="en">
<head>
<meta charset="utf-8">
<title>ZestRow Spices – Flavour Labels</title>
<link href="https://fonts.googleapis.com/css2?family=Bebas+Neue&family=Oswald:wght@500;600&display=swap" rel="stylesheet">
<style>
  :root {
    --stage: #d8d8d8;
    --label-black: #1d1d1e;
    --ink-white: #ffffff;
    --taco-blue: #3a6ea8;
    --coffee-brown: #9c6a3a;
    --garlic-green: #9bb83a;
    --curry-orange: #ee5a10;
    --chai-gold: #d9a129;
    --shadow: rgba(20, 20, 20, 0.75);
  }
  * { margin: 0; padding: 0; box-sizing: border-box; }
  html, body { width: 1200px; height: 813px; overflow: hidden; }
  body {
    background: radial-gradient(ellipse at center, #dedede 0%, var(--stage) 70%, #cfcfcf 100%);
    position: relative;
    font-family: "Bebas Neue", "Oswald", sans-serif;
  }
  .label {
    position: absolute;
    width: calc(255px * var(--s));
    height: calc(515px * var(--s));
    font-size: calc(10px * var(--s));
    color: var(--ink-white);
  }
  .label__shape { position: absolute; inset: 0; width: 100%; height: 100%; overflow: visible; }
  .label__shape .edge { fill: var(--accent); }
  .label__shape .panel { fill: var(--label-black); }
  .label__shadow {
    position: absolute;
    left: 50%;
    top: 104%;
    width: 64%;
    height: 1.4em;
    transform: translateX(-50%);
    border-radius: 50%;
    background: var(--shadow);
    filter: blur(calc(4px * var(--s)));
  }

  /* every block below is placed in label units (1em = label scale) */
  .slot {
    position: absolute;
    left: 0;
    right: 0;
    display: flex;
    align-items: center;
    justify-content: center;
    text-align: center;
  }
  .rule {
    position: absolute;
    height: 0;
    border-top: calc(2px * var(--s)) solid var(--ink-white);
  }
  .rule--dotted::after {
    content: "";
    position: absolute;
    left: 50%;
    top: -0.45em;
    width: 2.4em;
    height: 0.8em;
    transform: translateX(-50%);
    background:
      radial-gradient(circle, var(--ink-white) 0.3em, transparent 0.32em) 0 0 / 0.8em 0.8em repeat-x,
      var(--label-black);
  }
  .brand-mark {
    position: absolute;
    left: 11.75em;
    top: 5.2em;
    width: 2em;
    height: 2em;
    border-radius: 50%;
    background: var(--ink-white);
  }
  .rule--top-left  { left: 4em;    width: 6.8em; top: 6.2em; }
  .rule--top-right { left: 14.7em; width: 6.8em; top: 6.2em; }

  .slot--brand { top: 7.4em; height: 8.6em; }
  .brand-name {
    font-family: "Bebas Neue", sans-serif;
    font-size: 8.4em;
    line-height: 1;
    letter-spacing: 0.005em;
    color: var(--ink-white);
  }
  .brand-band {
    position: absolute;
    left: 6.6em;
    width: 12.3em;
    top: 15.9em;
    height: 1.9em;
    background: var(--accent);
    display: flex;
    align-items: center;
    justify-content: center;
  }
  .brand-band span {
    font-family: "Oswald", sans-serif;
    font-weight: 500;
    font-size: 1.3em;
    letter-spacing: 0.9em;
    padding-left: 0.9em;
    line-height: 1;
    color: var(--ink-white);
  }
  .slot--tagline { top: 18em; height: 1.6em; }
  .tagline {
    font-family: "Oswald", sans-serif;
    font-weight: 600;
    font-size: 1.15em;
    letter-spacing: 0.02em;
    line-height: 1;
    white-space: nowrap;
    color: var(--ink-white);
  }
  .rule--tagline { left: 6.6em; width: 12.3em; top: 20em; }

  .slot--flavour { top: 22em; height: 14.6em; }
  .flavour__name {
    font-family: "Bebas Neue", sans-serif;
    font-weight: 400;
    font-size: 7em;
    line-height: 0.88;
    color: var(--accent);
    letter-spacing: 0.005em;
  }

  .rule--bottom { left: 5em; width: 15.5em; top: 38.2em; }
  .slot--claim { top: 39.4em; height: 3em; }
  .claim {
    font-family: "Bebas Neue", sans-serif;
    font-size: 2.3em;
    line-height: 1;
    letter-spacing: 0.02em;
    color: var(--ink-white);
  }

  .label--taco   { --accent: var(--taco-blue);    --s: 0.682; left: 39px;  top: 230px; }
  .label--coffee { --accent: var(--coffee-brown); --s: 0.851; left: 235px; top: 208px; }
  .label--garlic { --accent: var(--garlic-green); --s: 1;     left: 478px; top: 189px; }
  .label--curry  { --accent: var(--curry-orange); --s: 0.851; left: 761px; top: 208px; }
  .label--chai   { --accent: var(--chai-gold);    --s: 0.682; left: 993px; top: 230px; }
</style>
</head>
<body>
  <main class="label-range">
    <article class="label label--taco">
      <div class="label__shadow"></div>
      <svg class="label__shape" viewBox="0 0 200 404" preserveAspectRatio="none" aria-hidden="true">
        <path class="edge" d="M0 0 H200 V290 C200 355 145 390 100 404 C55 390 0 355 0 290 Z"/>
        <path class="panel" d="M14 0 H186 V286 C186 340 138 370 100 382 C62 370 14 340 14 286 Z"/>
      </svg>
      <span class="brand-mark"></span>
      <span class="rule rule--top-left"></span><span class="rule rule--top-right"></span>
      <div class="slot slot--brand"><h2 class="brand-name">ZestRow</h2></div>
      <div class="brand-band"><span>SPICES</span></div>
      <div class="slot slot--tagline"><p class="tagline">WEIGHT LOSS SEASONINGS</p></div>
      <span class="rule rule--tagline rule--dotted"></span>
      <div class="slot slot--flavour"><h3 class="flavour__name">Taco</h3></div>
      <span class="rule rule--bottom rule--dotted"></span>
      <div class="slot slot--claim"><p class="claim">No Salt Added</p></div>
    </article>

    <article class="label label--coffee">
      <div class="label__shadow"></div>
      <svg class="label__shape" viewBox="0 0 200 404" preserveAspectRatio="none" aria-hidden="true">
        <path class="edge" d="M0 0 H200 V290 C200 355 145 390 100 404 C55 390 0 355 0 290 Z"/>
        <path class="panel" d="M14 0 H186 V286 C186 340 138 370 100 382 C62 370 14 340 14 286 Z"/>
      </svg>
      <span class="brand-mark"></span>
      <span class="rule rule--top-left"></span><span class="rule rule--top-right"></span>
      <div class="slot slot--brand"><h2 class="brand-name">ZestRow</h2></div>
      <div class="brand-band"><span>SPICES</span></div>
      <div class="slot slot--tagline"><p class="tagline">WEIGHT LOSS SEASONINGS</p></div>
      <span class="rule rule--tagline rule--dotted"></span>
      <div class="slot slot--flavour"><h3 class="flavour__name">Coffee<br>Rub</h3></div>
      <span class="rule rule--bottom rule--dotted"></span>
      <div class="slot slot--claim"><p class="claim">No Salt Added</p></div>
    </article>

    <article class="label label--garlic">
      <div class="label__shadow"></div>
      <svg class="label__shape" viewBox="0 0 200 404" preserveAspectRatio="none" aria-hidden="true">
        <path class="edge" d="M0 0 H200 V290 C200 355 145 390 100 404 C55 390 0 355 0 290 Z"/>
        <path class="panel" d="M14 0 H186 V286 C186 340 138 370 100 382 C62 370 14 340 14 286 Z"/>
      </svg>
      <span class="brand-mark"></span>
      <span class="rule rule--top-left"></span><span class="rule rule--top-right"></span>
      <div class="slot slot--brand"><h2 class="brand-name">ZestRow</h2></div>
      <div class="brand-band"><span>SPICES</span></div>
      <div class="slot slot--tagline"><p class="tagline">WEIGHT LOSS SEASONINGS</p></div>
      <span class="rule rule--tagline rule--dotted"></span>
      <div class="slot slot--flavour"><h3 class="flavour__name">Garlic<br>Oregano</h3></div>
      <span class="rule rule--bottom rule--dotted"></span>
      <div class="slot slot--claim"><p class="claim">No Salt Added</p></div>
    </article>

    <article class="label label--curry">
      <div class="label__shadow"></div>
      <svg class="label__shape" viewBox="0 0 200 404" preserveAspectRatio="none" aria-hidden="true">
        <path class="edge" d="M0 0 H200 V290 C200 355 145 390 100 404 C55 390 0 355 0 290 Z"/>
        <path class="panel" d="M14 0 H186 V286 C186 340 138 370 100 382 C62 370 14 340 14 286 Z"/>
      </svg>
      <span class="brand-mark"></span>
      <span class="rule rule--top-left"></span><span class="rule rule--top-right"></span>
      <div class="slot slot--brand"><h2 class="brand-name">ZestRow</h2></div>
      <div class="brand-band"><span>SPICES</span></div>
      <div class="slot slot--tagline"><p class="tagline">WEIGHT LOSS SEASONINGS</p></div>
      <span class="rule rule--tagline rule--dotted"></span>
      <div class="slot slot--flavour"><h3 class="flavour__name">Mild<br>Curry</h3></div>
      <span class="rule rule--bottom rule--dotted"></span>
      <div class="slot slot--claim"><p class="claim">No Salt Added</p></div>
    </article>

    <article class="label label--chai">
      <div class="label__shadow"></div>
      <svg class="label__shape" viewBox="0 0 200 404" preserveAspectRatio="none" aria-hidden="true">
        <path class="edge" d="M0 0 H200 V290 C200 355 145 390 100 404 C55 390 0 355 0 290 Z"/>
        <path class="panel" d="M14 0 H186 V286 C186 340 138 370 100 382 C62 370 14 340 14 286 Z"/>
      </svg>
      <span class="brand-mark"></span>
      <span class="rule rule--top-left"></span><span class="rule rule--top-right"></span>
      <div class="slot slot--brand"><h2 class="brand-name">ZestRow</h2></div>
      <div class="brand-band"><span>SPICES</span></div>
      <div class="slot slot--tagline"><p class="tagline">WEIGHT LOSS SEASONINGS</p></div>
      <span class="rule rule--tagline rule--dotted"></span>
      <div class="slot slot--flavour"><h3 class="flavour__name">Golden<br>Chai</h3></div>
      <span class="rule rule--bottom rule--dotted"></span>
      <div class="slot slot--claim"><p class="claim">No Salt Added</p></div>
    </article>
  </main>
</body>
</html>
```